we need PDF and print ready letterheads, dupplicated 5 times with different company details of different companies. All the companies are properties developments and no need for fancy logos (any reasonable shape is ok). Then simply change the companies details (names and company number) and the colour scheme slightly. I will supply the details.

The print ready should be 300dpi, and must have cropped marks.

Should be an easy job!

```html
<!DOCTYPE html>
<html lang="en">
<head>
<meta charset="utf-8">
<title>Letterhead</title>
<link rel="stylesheet" href="https://fonts.googleapis.com/css2?family=Jost:wght@500;600&family=Montserrat:wght@400;600&family=Open+Sans:wght@300;400;600&display=swap">
<style>
  :root {
    --ink: #1e1e1e;
    --text: #2b3338;
    --accent: #00f0ff;
    --brand: #1e8fef;
    --paper: #ffffff;
    --skyline-top: #5a5a5a;
    --skyline-bottom: #1e1e1e;
  }
  * { margin: 0; padding: 0; box-sizing: border-box; }
  html, body { width: 927px; height: 1200px; overflow: hidden; background: var(--paper); }
  .letterhead {
    position: relative; width: 927px; height: 1200px; overflow: hidden;
    background: var(--paper); color: var(--text);
    font-family: "Open Sans", Arial, sans-serif;
  }
  .band { position: absolute; top: 0; height: 220px; }
  .band--dark-left { left: 0; width: 93px; background: var(--ink); }
  .band--accent-left { left: 93px; width: 17px; background: var(--accent); }
  .band--accent-right { left: 817px; width: 17px; background: var(--accent); }
  .band--dark-right { left: 834px; width: 93px; background: var(--ink); }

  .brand-mark {
    position: absolute; left: 475px; top: 86px; width: 24px; height: 24px;
    background: var(--brand);
  }
  .company-name {
    position: absolute; left: 0; width: 974px; top: 138px; text-align: center;
    font-size: 35px; font-weight: 600; letter-spacing: 0.5px; color: var(--text);
  }

  .contact { position: absolute; right: 125px; top: 244px; text-align: right; }
  .contact__item {
    display: flex; justify-content: flex-end; align-items: center;
    height: 29px; font-size: 20px; color: var(--ink); white-space: nowrap;
  }
  .contact__item:last-child { margin-top: 6px; }
  .contact__item svg { width: 18px; height: 18px; margin-left: 14px; fill: var(--ink); }

  .headline {
    position: absolute; left: 131px; top: 293px;
    font-family: "Jost", Arial, sans-serif; font-weight: 600; font-size: 50px;
    letter-spacing: 1px; color: var(--text); line-height: 1.2;
  }
  .body-copy {
    position: absolute; left: 131px; font-weight: 300; color: var(--text); white-space: nowrap;
  }
  .body-copy span { display: block; }
  .body-copy--intro { top: 362px; font-size: 19px; line-height: 23.6px; }
  .body-copy--short { top: 508px; font-size: 20.5px; line-height: 25.6px; }
  .body-copy--main { top: 663px; font-size: 20.5px; line-height: 25.6px; }
  .subheading {
    position: absolute; left: 132px; top: 598px;
    font-family: "Jost", Arial, sans-serif; font-weight: 500; font-size: 30px;
    letter-spacing: 0.5px; color: var(--text);
  }

  .sign-off { position: absolute; left: 132px; top: 890px; font-size: 17px; color: var(--text); }
  .signature {
    position: absolute; left: 128px; top: 916px; width: 192px; height: 68px;
    background: linear-gradient(90deg, #eef0f1, #dfe3e5); border-radius: 4px;
  }
  .sign-title { position: absolute; left: 132px; top: 988px; font-size: 17px; color: var(--text); }

  .sender { position: absolute; right: 107px; top: 890px; text-align: right; font-family: "Montserrat", Arial, sans-serif; }
  .sender__name { font-weight: 600; font-size: 34px; line-height: 1.2; color: var(--ink); letter-spacing: 0.5px; }
  .sender__role { font-size: 20px; line-height: 1.1; color: var(--ink); letter-spacing: 0.5px; }
  .address {
    position: absolute; right: 92px; top: 980px; display: flex; align-items: center;
    font-size: 24px; color: var(--ink);
  }
  .address svg { width: 26px; height: 36px; margin-left: 12px; fill: var(--ink); }

  .skyline {
    position: absolute; left: 114px; top: 1048px; width: 813px; height: 152px;
    background: linear-gradient(180deg, var(--skyline-top), var(--skyline-bottom));
  }
</style>
</head>
<body>
<main class="letterhead">
  <div class="band band--dark-left"></div>
  <div class="band band--accent-left"></div>
  <div class="band band--accent-right"></div>
  <div class="band band--dark-right"></div>

  <div class="brand-mark"></div>
  <h1 class="company-name">COMPANY NAME</h1>

  <ul class="contact">
    <li class="contact__item">0312-555-014
      <svg viewBox="0 0 24 24"><path d="M6.6 10.8a15 15 0 0 0 6.6 6.6l2.2-2.2a1 1 0 0 1 1-.25 11.4 11.4 0 0 0 3.6.57 1 1 0 0 1 1 1V20a1 1 0 0 1-1 1A17 17 0 0 1 3 4a1 1 0 0 1 1-1h3.5a1 1 0 0 1 1 1c0 1.25.2 2.45.57 3.57a1 1 0 0 1-.25 1z"/></svg>
    </li>
    <li class="contact__item">@yourweb.com
      <svg viewBox="0 0 24 24"><path d="M2 5h20v14H2z M4 7v.5l8 5.5 8-5.5V7l-8 5.5z" fill-rule="evenodd"/></svg>
    </li>
    <li class="contact__item">www.yourweb.com
      <svg viewBox="0 0 24 24"><path d="M12 2a10 10 0 1 0 0 20 10 10 0 0 0 0-20zm0 2c.9 1.2 1.6 2.6 2 4h-4c.4-1.4 1.1-2.8 2-4zM4.3 14a8 8 0 0 1 0-4h3.4a16 16 0 0 0 0 4zm.9 2h3c.3 1.3.8 2.5 1.4 3.6A8 8 0 0 1 5.2 16zm3-8h-3a8 8 0 0 1 4.4-3.6C8.9 5.5 8.5 6.7 8.2 8zM12 20c-.9-1.2-1.6-2.6-2-4h4c-.4 1.4-1.1 2.8-2 4zm2.3-6H9.7a14 14 0 0 1 0-4h4.6a14 14 0 0 1 0 4zm.1 5.6c.6-1.1 1.1-2.3 1.4-3.6h3a8 8 0 0 1-4.4 3.6zM16.3 14a16 16 0 0 0 0-4h3.4a8 8 0 0 1 0 4zm-.5-6c-.3-1.3-.8-2.5-1.4-3.6A8 8 0 0 1 18.8 8z"/></svg>
    </li>
  </ul>

  <h2 class="headline">HEADLINE</h2>
  <p class="body-copy body-copy--intro">
    <span>Lorem ipsum dolor sit amet, consectetuer adipiscing elit, sed diam nonummy</span>
    <span>nibh euismod tincidunt ut laoreet dolore magna aliquam erat volutpat. Ut wisi</span>
    <span>enim ad minim veniam, quis nostrud exerci tation ullamcorper suscipit lobor-</span>
    <span>tis nisl ut aliquip ex ea commodo consequat. Duis autem vel eum iriure dolor</span>
    <span>in hendrerit in vulputate velit esse molestie consequat, vel illum dolore eu</span>
  </p>
  <p class="body-copy body-copy--short">
    <span>Lorem ipsum dolor sit amet, consectetuer adipiscing elit, sed diam</span>
    <span>nonummy nibh euismod tincidunt ut laoreet dolore magna aliquam erat</span>
  </p>

  <h3 class="subheading">PLACE YOUR TEXT HERE</h3>
  <p class="body-copy body-copy--main">
    <span>Lorem ipsum dolor sit amet, consectetuer adipiscing elit, sed diam</span>
    <span>nonummy nibh euismod tincidunt ut laoreet dolore magna aliquam erat</span>
    <span>volutpat. Ut wisi enim ad minim veniam, quis nostrud exerci tation</span>
    <span>ullamcorper suscipit lobortis nisl ut aliquip ex ea commodo consequat.</span>
    <span>Duis autem vel eum iriure dolor in hendrerit in vulputate velit esse mo-</span>
    <span>lestie consequat, vel illum dolore eu feugiat nulla facilisis at vero eros et</span>
  </p>

  <p class="sign-off">Regard</p>
  <div class="signature" role="img" aria-label="Handwritten signature"></div>
  <p class="sign-title">Art Director</p>

  <div class="sender">
    <p class="sender__name">Daniel Whitcombe</p>
    <p class="sender__role">Managing Member</p>
  </div>
  <p class="address">your address here
    <svg viewBox="0 0 24 34"><path d="M12 0A12 12 0 0 0 0 12c0 9 12 22 12 22s12-13 12-22A12 12 0 0 0 12 0zm0 17a5 5 0 1 1 0-10 5 5 0 0 1 0 10z"/></svg>
  </p>

  <div class="skyline" role="img" aria-label="City skyline silhouette along the bottom edge"></div>
</main>
</body>
</html>
```